New business Card Design

I'm looking to do a new design for our business cards.

Our Company its called the Garden quarter we are a High end outdoor Design and construction company based out of miami FL

Our Style is elegant, minimalist, Luxury but accessible.

see our Website: www.thegardenquarter-example.com

Attached find our logo as well as some samples the cards that we have for our sister company.

Sample Contact information ( in no particular order):

Marco Ventresca
VP of Sales and Marketing
Marco@thegardenquarter-example.com
555.204.7719
4172 NW 63 AVE Miami Florida, 33199

Designs are Looking Great guys but not quite there yet!

Upload your last few designs between today and Tomorrow. we will be choosing one on Saturday!

Cheers, 

Marco Ventresca
Director Of Marketing 

Hello Guys, 

Sorry we have not made a decision yet.  a lot of cool stuff! just narrowing down our options. 
expect a decision with in a day or 2. 

Marco. 

Target Market(s)

high End Design and construction. Luxurious but accessible

Industry/Entity Type

Construction

Colors

Designer to choose colors to be used in the design.

```html
<!DOCTYPE html>
<html lang="en">
<head>
<meta charset="utf-8">
<title>The Garden quarter — Business Cards</title>
<link href="https://fonts.googleapis.com/css2?family=Josefin+Sans:wght@400;600&display=swap" rel="stylesheet">
<style>
  :root {
    --backdrop: #e4e2de;
    --card: #ffffff;
    --card-shade: #f1f1f1;
    --ink: #2b2b2b;
    --ink-soft: #555555;
    --accent-blue: #1f7fc0;
    --accent-green: #6cae3c;
  }
  * { box-sizing: border-box; margin: 0; padding: 0; }
  html, body {
    width: 1200px; height: 871px; overflow: hidden;
    background: var(--backdrop);
    font-family: "Josefin Sans", sans-serif;
    color: var(--ink);
  }
  .canvas { position: relative; width: 1200px; height: 871px; }
  .card {
    position: absolute;
    width: 560px; height: 320px;
    background: linear-gradient(135deg, var(--card) 55%, var(--card-shade));
    box-shadow: 0 10px 28px rgba(0,0,0,0.25);
    overflow: hidden;
  }
  .card--front { left: 90px; top: 90px; }
  .card--back { left: 550px; top: 460px; }

  .brand {
    position: absolute; left: 0; right: 0; top: 0; bottom: 0;
    display: flex; flex-direction: column; align-items: center; justify-content: center;
    gap: 26px;
  }
  .brand__dot {
    width: 110px; height: 110px; border-radius: 50%;
    background: var(--accent-green);
  }
  .brand__name {
    font-size: 34px; font-weight: 600; letter-spacing: 3px;
    text-transform: uppercase; color: var(--ink);
  }

  .back-brand {
    position: absolute; left: 34px; top: 40px;
    font-size: 22px; font-weight: 600; letter-spacing: 2px;
    text-transform: uppercase; color: var(--accent-green);
    line-height: 1.25; width: 180px;
  }

  .contact {
    position: absolute; right: 40px; top: 90px;
    text-align: right; letter-spacing: 1.6px;
  }
  .contact__name { font-size: 15px; font-weight: 600; color: var(--ink); }
  .contact__title { font-size: 13px; color: var(--accent-blue); margin-top: 4px; }
  .contact__address { font-size: 11.5px; color: var(--ink-soft); margin-top: 20px; }
  .contact__list { list-style: none; margin-top: 24px; }
  .contact__item {
    display: flex; justify-content: flex-end; align-items: center; gap: 14px;
    font-size: 11.5px; color: var(--ink-soft); height: 22px;
  }
  .contact__icon { width: 12px; height: 12px; fill: var(--accent-green); }
</style>
</head>
<body>
<main class="canvas">
  <section class="card card--front" aria-label="Card front">
    <div class="brand">
      <span class="brand__dot"></span>
      <span class="brand__name">The Garden quarter</span>
    </div>
  </section>

  <section class="card card--back" aria-label="Card back">
    <div class="back-brand">The Garden quarter</div>
    <div class="contact">
      <p class="contact__name">Marco Ventresca</p>
      <p class="contact__title">VP of Sales and Marketing</p>
      <p class="contact__address">4172 NW 63 AVE Miami Florida, 33199</p>
      <ul class="contact__list">
        <li class="contact__item">555.204.7719
          <svg class="contact__icon" viewBox="0 0 12 12" aria-hidden="true"><path d="M2 1h2.5l1 3-1.5 1a6 6 0 0 0 3 3l1-1.5 3 1V10a1 1 0 0 1-1 1A9 9 0 0 1 1 2a1 1 0 0 1 1-1z"/></svg>
        </li>
        <li class="contact__item">Marco@thegardenquarter-example.com
          <svg class="contact__icon" viewBox="0 0 12 12" aria-hidden="true"><path d="M1 3h10v6H1z M1 3l5 3.5L11 3" stroke="#fff" stroke-width="0.8"/></svg>
        </li>
        <li class="contact__item">www.thegardenquarter-example.com
          <svg class="contact__icon" viewBox="0 0 12 12" aria-hidden="true"><circle cx="6" cy="6" r="5"/><path d="M1 6h10M6 1c-2 3-2 7 0 10M6 1c2 3 2 7 0 10" stroke="#fff" stroke-width="0.7" fill="none"/></svg>
        </li>
      </ul>
    </div>
  </section>
</main>
</body>
</html>
```